Lawn care business card

I am looking for a quality designed personal business card to represent the quality and elegant nature of our company. We separate ourselves in our market by the aesthetic value of our work, so I am looking for marketing material that does the same. We target our marketing high end customers, and we try to avoid price shoppers. I am open to all design options, so long as they are in line with our companies values.

We are tend to go with a retro look on everything from our logo and print material, to our uniforms. We like to portray and "old fashion" set of core values, with a modern elegance. So a wild and crazy look is out of the question.

Things I'd like on the card:
1.) Logo
2.) Phone number: (816) 555-0193
3.) Website: Verdanthollow.com
4.) Email: peterwalsh@verdanthollow.com
5.) My name: Peter Walsh
6.) Facebook link: facebook.com/GreenridgeLawnandLandscape
7.) Instagram: http://instagram.com/verdanthollow

Attached is a copy of our logo.

```html
<!DOCTYPE html>
<html lang="en">
<head>
<meta charset="utf-8">
<title>Verdant Hollow – Business Card</title>
<link href="https://fonts.googleapis.com/css2?family=Saira:wght@300;400;500;600;700&display=swap" rel="stylesheet">
<style>
  :root {
    --orange: #e85a1a;
    --ink: #1c1c1c;
    --card: #f0f1f0;
    --page: #ffffff;
    --trim: #9a9a9a;
    --label: #e8373a;
    --text: #2a2a2a;
  }
  html, body {
    margin: 0;
    padding: 0;
    width: 1136px;
    height: 1200px;
    overflow: hidden;
    background: var(--page);
    font-family: "Saira", "Helvetica Neue", Arial, sans-serif;
  }
  .sheet { position: relative; width: 1136px; height: 1200px; }
  .card {
    position: absolute;
    left: 2px;
    width: 910px;
    height: 560px;
    background: var(--card);
    border: 2px dotted var(--trim);
    box-sizing: border-box;
    overflow: hidden;
  }
  .card--front { top: 2px; }
  .card--back { top: 630px; }

  .side-label {
    position: absolute;
    left: 983px;
    font-weight: 300;
    font-size: 44px;
    letter-spacing: 1px;
    color: var(--label);
    margin: 0;
  }
  .side-label--front { top: 480px; }
  .side-label--back { top: 1115px; }

  .company-name {
    position: absolute;
    margin: 0;
    font-weight: 500;
    font-size: 31px;
    color: var(--orange);
    white-space: nowrap;
  }
  .card--front .company-name { left: 71px; top: 130px; }
  .card--back .company-name { left: 0; right: 0; top: 368px; text-align: center; }

  .brand-mark {
    position: absolute;
    display: flex;
    align-items: center;
    gap: 16px;
  }
  .brand-mark__dot {
    width: 70px;
    height: 70px;
    border-radius: 50%;
    background: var(--orange);
    flex: none;
  }
  .brand-mark__name {
    font-weight: 700;
    font-size: 30px;
    color: var(--ink);
    white-space: nowrap;
  }
  .card--front .brand-mark { left: 540px; top: 196px; }
  .card--back .brand-mark { left: 0; right: 0; top: 210px; justify-content: center; }

  .person-name {
    position: absolute;
    left: 71px;
    top: 260px;
    margin: 0;
    font-weight: 400;
    font-size: 34px;
    color: var(--orange);
  }
  .person-title {
    position: absolute;
    left: 79px;
    top: 297px;
    margin: 0;
    font-size: 20px;
    color: var(--text);
  }
  .contact-list {
    position: absolute;
    left: 80px;
    top: 362px;
    margin: 0;
    padding: 0;
    list-style: none;
    font-size: 20px;
    line-height: 35px;
    color: var(--text);
  }
  .social-band {
    position: absolute;
    left: 0;
    right: 0;
    bottom: 0;
    height: 82px;
    display: flex;
  }
  .social-band__item {
    display: flex;
    align-items: center;
    gap: 22px;
    color: #ffffff;
    font-size: 20px;
  }
  .social-band__item--facebook { width: 528px; background: var(--orange); padding-left: 113px; box-sizing: border-box; }
  .social-band__item--instagram { flex: 1; background: var(--ink); padding-left: 600px; padding-left: 72px; box-sizing: border-box; }
  .social-band__square {
    width: 32px;
    height: 32px;
    background: #ffffff;
    border-radius: 3px;
    flex: none;
  }
</style>
</head>
<body>
<main class="sheet">
  <section class="card card--front">
    <h1 class="company-name">VERDANT HOLLOW LAWN LANSCAPE</h1>
    <div class="brand-mark">
      <span class="brand-mark__dot"></span>
      <span class="brand-mark__name">VERDANT HOLLOW</span>
    </div>
    <h2 class="person-name">Peter Walsh</h2>
    <p class="person-title">Director</p>
    <ul class="contact-list">
      <li>M: (816) 555-0193</li>
      <li>E: peterwalsh@verdanthollow.com</li>
      <li>W: www.peterwalsh@verdanthollow.com</li>
    </ul>
    <div class="social-band">
      <div class="social-band__item social-band__item--facebook">
        <span class="social-band__square"></span>
        <span>GreenridgeLawnandLandscape</span>
      </div>
      <div class="social-band__item social-band__item--instagram">
        <span class="social-band__square"></span>
        <span>verdanthollow</span>
      </div>
    </div>
  </section>
  <p class="side-label side-label--front">FRONT</p>

  <section class="card card--back">
    <div class="brand-mark">
      <span class="brand-mark__dot"></span>
      <span class="brand-mark__name">VERDANT HOLLOW</span>
    </div>
    <h2 class="company-name">VERDANT HOLLOW LAWN LANSCAPE</h2>
  </section>
  <p class="side-label side-label--back">BACK</p>
</main>
</body>
</html>
```